Dune Business Card Design Project

We have an existing business card. We are looking to creat a new card for the store. I have attached a my own business so you have a refference of what the current card looks like.

Phone: 1300 574 213
email: merrow@dunepanes.com.au
website: www.dunepanes.com.au
Address: (Inside Merrow Rug Hall) 418 Tolvey Rd, Pelbrook VIC 3158
Updates

This is a new business card for our store.

Industry/Entity Type

Business

Requirements
Must have
• Must look similar to the existing card

```html
<!DOCTYPE html>
<html lang="en">
<head>
<meta charset="utf-8">
<title>Dune Shutters &amp; Blinds — Business Card</title>
<link rel="stylesheet" href="https://fonts.googleapis.com/css2?family=Lato:wght@300;400;700&display=swap">
<style>
  :root {
    --page-bg: #e9e6e1;
    --card-black: #141414;
    --card-white: #ffffff;
    --brand-red: #d0202a;
    --ink-dark: #1b1b1b;
    --ink-grey: #6d6d6d;
    --ink-light: #f2f2f2;
    --ghost: #2a2a2a;
  }
  * { box-sizing: border-box; margin: 0; padding: 0; }
  html, body {
    width: 1200px; height: 1000px; overflow: hidden;
    background: var(--page-bg);
    font-family: "Lato", Arial, sans-serif;
  }
  .canvas { position: relative; width: 1200px; height: 1000px; }

  .card {
    position: absolute; left: 250px; width: 700px; height: 428px;
    border-radius: 16px; overflow: hidden;
    box-shadow: 0 10px 28px rgba(0,0,0,0.25);
  }

  /* Front */
  .card-front { top: 50px; background: var(--card-black); }
  .front-brand { position: absolute; left: 170px; top: 70px; color: var(--card-white); }
  .front-brand .wordmark {
    font-weight: 300; font-size: 170px; line-height: 1; letter-spacing: 2px;
  }
  .front-brand .tagline {
    font-weight: 700; font-size: 34px; margin-top: 6px; margin-left: 40px;
  }
  .front-url {
    position: absolute; left: 0; right: 0; top: 330px; text-align: center;
    color: var(--brand-red); font-weight: 700; font-size: 19px; letter-spacing: 0.5px;
  }

  /* Back */
  .card-back { top: 520px; background: var(--card-black); }
  .back-header {
    position: absolute; left: 0; top: 0; width: 100%; height: 150px;
    background: var(--card-white);
  }
  .back-band {
    position: absolute; left: 0; top: 150px; width: 100%; height: 14px;
    background: var(--brand-red);
  }
  .back-brand { position: absolute; left: 40px; top: 12px; }
  .back-brand .wordmark {
    font-weight: 300; font-size: 96px; line-height: 1; color: var(--ink-dark);
  }
  .back-brand .tagline {
    font-weight: 700; font-size: 22px; color: var(--ink-grey); margin-top: 2px;
  }
  .contact { position: absolute; left: 40px; top: 196px; color: var(--ink-light); }
  .contact .name {
    color: var(--brand-red); font-weight: 700; font-size: 23px; text-transform: uppercase;
  }
  .contact .role { font-size: 19px; margin-top: 2px; }
  .contact .lines { margin-top: 18px; font-size: 17px; line-height: 1.7; }
  .contact .label { color: var(--brand-red); font-weight: 700; margin-right: 4px; }
  .contact .address { margin-top: 14px; font-size: 17px; line-height: 1.35; }

  .ghost-brand { position: absolute; right: 50px; top: 218px; color: var(--ghost); }
  .ghost-brand .wordmark { font-weight: 300; font-size: 104px; line-height: 1; }
  .ghost-brand .tagline { font-weight: 700; font-size: 22px; margin-top: 2px; }
</style>
</head>
<body>
<main class="canvas">
  <section class="card card-front" aria-label="Card front">
    <div class="front-brand">
      <div class="wordmark">dune</div>
      <div class="tagline">Shutters &amp; Blinds</div>
    </div>
    <div class="front-url">www.dunepanes.com.au</div>
  </section>

  <section class="card card-back" aria-label="Card back">
    <div class="back-header"></div>
    <div class="back-band"></div>
    <div class="back-brand">
      <div class="wordmark">dune</div>
      <div class="tagline">Shutters &amp; Blinds</div>
    </div>
    <div class="ghost-brand" aria-hidden="true">
      <div class="wordmark">dune</div>
      <div class="tagline">Shutters &amp; Blinds</div>
    </div>
    <div class="contact">
      <div class="name">Aaron Tellis</div>
      <div class="role">Director</div>
      <div class="lines">
        <div><span class="label">P:</span>1300 574 213</div>
        <div><span class="label">E:</span>merrow@dunepanes.com.au</div>
      </div>
      <div class="address">(Inside Merrow Rug Hall) 418<br>Tolvey Rd, Pelbrook VIC 3158</div>
    </div>
  </section>
</main>
</body>
</html>
```